Dune Loop needs some awesome stationary

Do you have what it takes to get my brand? You either do or you don't, have a crack at a design and you my just win my business.

I don't want to waste your or my time, so put your creative genius on either a business card or envelope.

I however need a package of stationary that follows the same brand. I will message you to complete the remaining should I like your first submission.

Here is what I need, have a go!

Basically I need the following for my small business based in melbourne.
- Letterhead (printer ready and MS Word)
- Business Card
- Compliments Slip
- Envelope
- Proposal Cover Page (MS Word only)
- Presentation Folder
- Harbor Tally Cards
- Student Name Tent
- Index Cards
- Tack-Pad

I am establishing the brand and it must be modern, professional but also relaxed; that is not formal and not corporate. It represents a company are leaders, but small enough to care and operate like a bunch of friends. We are bringing people and conversations back to business, and turfing out all the bureaucracy and crazy and wasteful procedures. Its about "lets talk and figure it out together and find even better ways".

Target Market(s)

Mainly companies that build software products, but Agile practices are used in many other industries (even graphic design projects)

Industry/Entity Type

Information Technology

Font styles to use
Sans Serif

Colors
3176b5
aaaaaa

Requirements
Must have
• I like curves and circles and not boxes or rectangles.
• I want a colour rich design with my brand colours, but it must be balanced.
• I want more modern than traditional, but simple modern
Should not have
• Not corporate
• Please don't waste my time if your not going to think about it.
• Don't mess with my primary logo
• Don't change my colours
• Don't overlay logo on image

```html
<!DOCTYPE html>
<html lang="en">
<head>
<meta charset="utf-8">
<title>Dune Loop – Business Card</title>
<link href="https://fonts.googleapis.com/css2?family=Open+Sans:wght@300;400;600;700&family=Roboto+Condensed:wght@700&display=swap" rel="stylesheet">
<style>
  :root{
    --backdrop:#7fb0f0;
    --card:#2d62ab;
    --card-deep:#22518f;
    --band:#1d4a88;
    --grey:#aaaaaa;
    --white:#ffffff;
    --ink-soft:#dfe8f5;
  }
  *{box-sizing:border-box;margin:0;padding:0}
  html,body{width:1200px;height:790px;overflow:hidden}
  body{background:var(--backdrop);font-family:"Open Sans",sans-serif;position:relative}

  .card{position:absolute;width:480px;height:292px;background:var(--card);
        box-shadow:0 14px 30px rgba(20,50,110,.35);overflow:hidden}
  .card--front{left:75px;top:249px}
  .card--back{left:645px;top:249px}

  /* front */
  .front__brand{position:absolute;left:0;top:0;width:184px;height:100%;
        border-right:1px solid var(--card-deep);
        display:flex;flex-direction:column;align-items:center;justify-content:center;gap:8px}
  .brand-mark{display:flex;align-items:center;gap:10px}
  .brand-mark__dot{width:30px;height:30px;border-radius:50%;background:var(--grey)}
  .brand-mark__name{font-weight:700;font-size:26px;color:var(--white);letter-spacing:.3px}
  .front__entity{font-family:"Roboto Condensed",sans-serif;font-weight:700;font-size:15px;color:var(--white)}

  .front__details{position:absolute;left:184px;top:0;right:0;bottom:0}
  .name-band{position:absolute;left:14px;right:0;top:30px;height:62px;background:var(--band);
        border-radius:31px 0 0 31px;padding:10px 22px 0 0;text-align:right}
  .name-band__name{font-weight:700;font-size:17px;letter-spacing:3px;color:var(--white);text-transform:uppercase}
  .name-band__title{font-weight:300;font-size:12px;letter-spacing:1px;color:var(--ink-soft);font-variant:small-caps}

  .contact{position:absolute;right:22px;top:116px;list-style:none;text-align:right}
  .contact li{display:flex;justify-content:flex-end;align-items:center;gap:10px;
        font-size:11px;line-height:19px;color:var(--ink-soft)}
  .contact li.contact__strong{font-weight:700;color:var(--white)}
  .contact svg{width:11px;height:11px;flex:none}
  .contact .no-icon{width:11px;flex:none}

  /* back */
  .back__brand{position:absolute;inset:0;display:flex;align-items:center;justify-content:center}
  .back__brand .brand-mark__dot{width:44px;height:44px}
  .back__brand .brand-mark__name{font-size:36px}
  .rule{position:absolute;height:2px;width:78px;background:var(--white)}
  .rule--top{left:0;top:62px}
  .rule--bottom{right:0;bottom:62px}
</style>
</head>
<body>

<section class="card card--front" aria-label="Business card front">
  <div class="front__brand">
    <div class="brand-mark">
      <span class="brand-mark__dot"></span>
      <span class="brand-mark__name">Dune Loop</span>
    </div>
    <div class="front__entity">Dune Loop Pty Ltd</div>
  </div>

  <div class="front__details">
    <div class="name-band">
      <div class="name-band__name">Jarrah Pellow</div>
      <div class="name-band__title">CEO, Agile Coach &amp; Trainer</div>
    </div>

    <ul class="contact">
      <li class="contact__strong">1300DUNES
        <svg viewBox="0 0 12 12"><path fill="#fff" d="M2.5 1h2l1 2.5-1.3 1a6 6 0 0 0 3.3 3.3l1-1.3 2.5 1v2c0 .6-.5 1-1 1A9.5 9.5 0 0 1 1.5 2c0-.5.4-1 1-1z"/></svg></li>
      <li>+61 400 555 012
        <svg viewBox="0 0 12 12"><rect x="3" y="0.5" width="6" height="11" rx="1.2" fill="none" stroke="#fff"/><circle cx="6" cy="9.6" r=".7" fill="#fff"/></svg></li>
      <li>jarrah@duneloop.com.au
        <svg viewBox="0 0 12 12"><rect x="0.5" y="2.5" width="11" height="7" fill="none" stroke="#fff"/><path d="M.5 2.5 6 6.5l5.5-4" fill="none" stroke="#fff"/></svg></li>
      <li>www.duneloop.com.au
        <svg viewBox="0 0 12 12"><circle cx="6" cy="6" r="5.2" fill="none" stroke="#fff"/><ellipse cx="6" cy="6" rx="2.3" ry="5.2" fill="none" stroke="#fff"/><path d="M.8 6h10.4" stroke="#fff"/></svg></li>
      <li>PO Box 1402, Kelvin Grove,<span class="no-icon"></span></li>
      <li>VIC 3199, Australia
        <svg viewBox="0 0 12 12"><path fill="#fff" d="M6 .5a4 4 0 0 1 4 4c0 3-4 7-4 7s-4-4-4-7a4 4 0 0 1 4-4z"/><circle cx="6" cy="4.5" r="1.4" fill="#2d62ab"/></svg></li>
    </ul>
  </div>
</section>

<section class="card card--back" aria-label="Business card back">
  <span class="rule rule--top"></span>
  <div class="back__brand">
    <div class="brand-mark">
      <span class="brand-mark__dot"></span>
      <span class="brand-mark__name">Dune Loop</span>
    </div>
  </div>
  <span class="rule rule--bottom"></span>
</section>

</body>
</html>
```